Veltaro Clear Springs needs a new business card design (we produce and sell pure bottled water)

We need a clean modern design for our new business cards, We have an existing logo which ultimately cannot be changed, however it could be slighty improved and the colours adjusted. We have this existing logo on all of our bottles, vehicles etc.

Our company slogan is "Fresh from source to sip".
Along with our relevant company information
(Address, phone, website email etc) we will only be using names and not putting position titles for flexibilty.

We are looking for a clean, minimalist modern design.

You can view our website (if need of an update also!) to see our business.

Contact Information for Business Card

Staff Name : XXXXXX XXXXXX
Address : 8/41 Dunmore St
Halden Flats QLD 4261
Staff Mobile Number : 04XX XXX XXX
Office Phone Number : 07 3915 2047
Staff Email Address : XXXX@veltaroclearsprings.com.au
Website : www.veltaroclearsprings.com.au

Font styles to use
Sans Serif

Colors
cee9f5
33a6d7
0492cd
0455a3
3276b5
85abd2
cedeed

Requirements
Must have
• The ability to edit and change the staff members details as we will need to edit for each respective staff member (7 in total)

```html
<!DOCTYPE html>
<html lang="en">
<head>
<meta charset="utf-8">
<title>Veltaro Clear Springs – Business Card</title>
<link href="https://fonts.googleapis.com/css2?family=Roboto:wght@300;400;700;900&display=swap" rel="stylesheet">
<style>
  :root {
    --navy: #2d2a86;
    --navy-deep: #24216f;
    --navy-light: #3a37a6;
    --white: #ffffff;
    --stage: #202024;
  }
  * { box-sizing: border-box; margin: 0; padding: 0; }
  html, body {
    width: 1200px; height: 900px; overflow: hidden;
    background: var(--stage);
    font-family: "Roboto", Arial, sans-serif;
  }
  .card {
    position: absolute; left: 290px;
    width: 620px; height: 354px;
    border-radius: 26px; overflow: hidden;
    background: var(--white);
  }
  .card--front { top: 62px; }
  .card--back  { top: 484px; }

  /* Front */
  .brand {
    position: absolute; left: 0; right: 0; top: 122px;
    display: flex; align-items: center; justify-content: center; gap: 14px;
  }
  .brand__mark { width: 26px; height: 26px; border-radius: 50%; background: var(--navy); flex: none; }
  .brand__name {
    font-weight: 900; font-size: 30px; color: var(--navy);
    text-transform: uppercase; letter-spacing: 0.5px;
  }
  .front-band {
    position: absolute; left: 0; right: 0; bottom: 0; height: 84px;
    background: linear-gradient(90deg, var(--navy-deep), var(--navy-light));
    clip-path: polygon(0 30px, 100% 0, 100% 100%, 0 100%);
  }
  .front-band__web {
    position: absolute; left: 0; right: 0; bottom: 24px; text-align: center;
    color: var(--white); font-size: 14px; font-weight: 300; letter-spacing: 0.6px;
  }

  /* Back */
  .back-panel {
    position: absolute; inset: 0;
    background: linear-gradient(160deg, var(--navy-light), var(--navy-deep));
    clip-path: polygon(0 0, 56% 0, 61% 100%, 0 100%);
  }
  .staff { position: absolute; left: 40px; top: 46px; color: var(--white); }
  .staff__name { font-size: 25px; font-weight: 700; letter-spacing: 1px; text-transform: uppercase; margin-bottom: 20px; }
  .contact { list-style: none; }
  .contact__item {
    display: flex; align-items: center; gap: 12px;
    font-size: 14px; font-weight: 300; line-height: 25px;
  }
  .contact__icon { width: 15px; height: 15px; flex: none; }
  .address {
    position: absolute; left: 40px; bottom: 36px;
    color: var(--white); font-size: 15px; font-weight: 300; line-height: 21px;
  }
  .back-brand {
    position: absolute; left: 61%; right: 0; top: 84px;
    display: flex; flex-direction: column; align-items: center; gap: 12px;
  }
  .back-brand .brand__mark { width: 30px; height: 30px; }
  .back-brand .brand__name { font-size: 25px; text-align: center; line-height: 29px; }
  .slogan-band {
    position: absolute; left: 64%; right: 0; top: 254px; height: 46px;
    background: var(--navy);
    display: flex; align-items: center; justify-content: center;
  }
  .slogan { color: var(--white); font-size: 13px; font-weight: 400; letter-spacing: 2px; white-space: nowrap; }
</style>
</head>
<body>

<section class="card card--front">
  <div class="brand">
    <span class="brand__mark"></span>
    <span class="brand__name">Veltaro Clear Springs</span>
  </div>
  <div class="front-band"></div>
  <span class="front-band__web">www.veltaroclearsprings.com.au</span>
</section>

<section class="card card--back">
  <div class="back-panel"></div>

  <div class="staff">
    <h1 class="staff__name">Marcus Reilly</h1>
    <ul class="contact">
      <li class="contact__item">
        <svg class="contact__icon" viewBox="0 0 16 16" fill="none" stroke="#fff" stroke-width="1.3"><rect x="4" y="1" width="8" height="14" rx="1.5"/><line x1="7" y1="12.5" x2="9" y2="12.5"/></svg>
        04XX XXX XXX
      </li>
      <li class="contact__item">
        <svg class="contact__icon" viewBox="0 0 16 16" fill="none" stroke="#fff" stroke-width="1.3"><path d="M3 2l3 0 1 3-2 1.5c1 2 2.5 3.5 4.5 4.5L11 9l3 1v3c-6 0.5-11.5-5-11-11z"/></svg>
        07 3915 2047
      </li>
      <li class="contact__item">
        <svg class="contact__icon" viewBox="0 0 16 16" fill="none" stroke="#fff" stroke-width="1.3"><rect x="1" y="3" width="14" height="10"/><path d="M1 3l7 6 7-6M1 13l5-5M15 13l-5-5"/></svg>
        XXXX@veltaroclearsprings.com.au
      </li>
      <li class="contact__item">
        <svg class="contact__icon" viewBox="0 0 16 16" fill="none" stroke="#fff" stroke-width="1.2"><circle cx="8" cy="8" r="6.5"/><ellipse cx="8" cy="8" rx="3" ry="6.5"/><line x1="1.5" y1="8" x2="14.5" y2="8"/></svg>
        www.veltaroclearsprings.com.au
      </li>
    </ul>
  </div>

  <p class="address">8/41 Dunmore St<br>Halden Flats QLD 4261</p>

  <div class="back-brand">
    <span class="brand__mark"></span>
    <span class="brand__name">Veltaro<br>Clear Springs</span>
  </div>

  <div class="slogan-band">
    <span class="slogan">Fresh from source to sip</span>
  </div>
</section>

</body>
</html>
```